Flyer for Programming Classes for Kids

We are small school in Tokyo, Japan teaching computer programming to kids in English.
We need a flyer to promote our classes and provide basic information about our company.
See Flyer_Notes.doc for more company info, class info, and flyer requirements.
Basic Info:
One page flyer. Two-sided, front and back.
We would like a flyer that introduces the company. -and-
Highlights the classes we offer
Target Market: 6-12 year old kids and their parents. Audience is English speaking families in Japan.
Look And Feel: Bold, Playful, Modern, Conservative
Paper Size: B4
What is B4? https://www.quorvanta.com/products/resources/paper-sizes-and-formats-explained.php
Target Market(s)
Tokyo, but English speakers
Industry/Entity Type
Education
Colors
Designer to choose colors to be used in the design.
Look and feel
Each slider illustrates characteristics of the customer's brand and the style your logo design should communicate.

```html
<!DOCTYPE html>
<html lang="en">
<head>
<meta charset="utf-8">
<title>Bytesprout – Coding Classes for Kids</title>
<link href="https://fonts.googleapis.com/css2?family=Montserrat:wght@700;800;900&family=Lato:wght@400;700&display=swap" rel="stylesheet">
<style>
  :root{
    --green:#a4d13a;
    --charcoal:#555557;
    --grey-head:#8a8a8c;
    --ink:#3b3b3d;
    --white:#ffffff;
    --stage:#b9b9bb;
    --photo-dark:#4a4844;
    --photo-mid:#8c8a86;
  }
  *{margin:0;padding:0;box-sizing:border-box}
  html,body{width:1200px;height:1200px;overflow:hidden;background:var(--stage)}
  body{position:relative;font-family:'Lato',sans-serif;color:var(--ink)}
  .page{position:absolute;width:526px;height:743px;overflow:hidden}
  .front{left:56px;top:159px;background:var(--white)}
  .back{left:614px;top:295px;background:var(--charcoal)}
  .page svg.shape{position:absolute;left:0;top:0}
  .abs{position:absolute}

  .brand{font-family:'Lato',sans-serif;font-weight:700;color:var(--green);letter-spacing:1px;line-height:1}
  .front .brand{left:27px;top:52px;width:240px;text-align:center;font-size:40px}
  .tagline{left:27px;top:96px;width:240px;text-align:center;font-size:10px;color:var(--ink);letter-spacing:.3px}

  .headline{left:26px;top:150px;font-family:'Montserrat',sans-serif;font-weight:900;font-size:47px;line-height:45px;color:var(--grey-head);letter-spacing:-.5px}
  .headline .accent{color:var(--green)}
  .ages{left:26px;top:335px;width:190px;height:48px;border-radius:6px;background:var(--green);color:var(--white);font-family:'Montserrat',sans-serif;font-weight:800;font-size:30px;line-height:48px;text-align:center}
  .taught{left:27px;top:421px;font-family:'Montserrat',sans-serif;font-weight:700;font-size:21px;color:var(--ink)}
  .enroll{left:26px;top:455px;width:268px;height:73px;background:var(--charcoal);border-radius:6px 0 0 6px;padding:12px 0 0 14px;font-family:'Montserrat',sans-serif;font-weight:800;font-size:24px;line-height:25px;color:var(--white)}
  .enroll .accent{color:var(--green)}

  .contact{left:27px;top:565px;width:260px;font-size:12.5px;line-height:15.5px}
  .contact h3{font-size:15.5px;font-weight:700;margin-bottom:6px}
  .contact p{margin-bottom:6px}
  .contact .phones{font-size:16px;font-weight:700;line-height:19px;margin:8px 0 6px}

  .intro{left:26px;width:192px;color:var(--white);font-size:12.6px;line-height:16.4px}
  .intro p{margin-bottom:4px}
  .intro-a{top:55px}
  .intro-b{top:426px;width:180px}
  .back .brand{left:26px;top:672px;font-size:34px}

  .classes{left:274px;top:54px;width:232px}
  .classes h2{font-family:'Montserrat',sans-serif;font-weight:800;font-size:19px;line-height:24px;color:var(--green);margin-bottom:6px}
  .classes ul{list-style:none;margin-bottom:14px}
  .classes li{font-size:11.8px;line-height:14.2px;padding-left:9px;position:relative;margin-bottom:5px}
  .classes li::before{content:"";position:absolute;left:0;top:6px;width:4px;height:4px;border-radius:50%;background:var(--ink)}
</style>
</head>
<body>

<section class="page front">
  <svg class="shape" width="526" height="743" viewBox="0 0 526 743">
    <defs>
      <linearGradient id="photoTop" x1="0" y1="0" x2="1" y2="1">
        <stop offset="0" stop-color="#4a4844"/><stop offset="1" stop-color="#8c8a86"/>
      </linearGradient>
      <linearGradient id="photoBottom" x1="0" y1="0" x2="1" y2="1">
        <stop offset="0" stop-color="#7a7874"/><stop offset="1" stop-color="#4d4b48"/>
      </linearGradient>
    </defs>
    <rect x="240" y="0" width="286" height="370" fill="url(#photoTop)" role="img" aria-label="Photo of a child coding on a laptop at a classroom desk"/>
    <rect x="240" y="370" width="286" height="373" fill="url(#photoBottom)" role="img" aria-label="Photo of a young girl working on a laptop in class"/>
    <path d="M0 0H238C288 0 304 40 304 120V280C304 336 340 366 390 370C340 374 304 404 304 460V640C304 712 272 743 232 743H0Z" fill="var(--green)"/>
    <path d="M0 0H224C272 0 290 40 290 120V280C290 340 328 368 372 370C328 372 290 400 290 460V640C290 710 260 743 220 743H0Z" fill="var(--white)"/>
  </svg>

  <div class="abs brand">bytesprout</div>
  <div class="abs tagline">Little Fingers, Big Ideas</div>

  <h1 class="abs headline">CODING<br>CLASSES<br><span class="accent">FOR<br>KIDS!</span></h1>
  <div class="abs ages">AGES 6–12</div>
  <div class="abs taught">Taught in English</div>
  <div class="abs enroll"><span class="accent">Enroll</span> for Summer<br>Camps <span class="accent">Now!</span></div>

  <div class="abs contact">
    <h3>Contact Info:</h3>
    <p>Close to Hanamori &amp; Kitazono Stations<br>3-14-7 Maple Court Hanamori 2F<br>Shibuya-ku Hanamori, Tokyo 150-0099</p>
    <p>hello@bytesprout.jp</p>
    <p class="phones">070-5831-2046 (Japanese)<br>070-5831-2098 (English)</p>
    <p>http://bytesprout.jp</p>
  </div>
</section>

<section class="page back">
  <svg class="shape" width="526" height="743" viewBox="0 0 526 743">
    <path d="M298 0C250 0 236 40 236 110V280C236 336 210 364 166 371C210 378 236 406 236 462V650C236 710 252 743 300 743H526V0Z" fill="var(--green)"/>
    <path d="M310 0C262 0 248 40 248 110V280C248 338 224 366 184 371C224 376 248 404 248 462V650C248 708 266 743 314 743H526V0Z" fill="var(--white)"/>
  </svg>

  <div class="abs intro intro-a">
    <p>Bytesprout is a programming school for kids, run by educators with professional software development experience. We have locations in Tokyo and in Singapore, which has received numerous awards. All lessons are taught in English. We provide coding classes for kids 6-17, form Beginner to Advanced. We think all kids should have the chance to learn to program and have fun doing it.</p>
    <p>Classes can be taught at our classrooms or at your institution. Weekly classes and week-long camps are offered.</p>
  </div>
  <div class="abs intro intro-b">
    <p>Our curriculum is based on STEM (Science, Technology, Engineering, and Math) with a pinch of Art, and whole lot of creativity. Kids learn core, computer science fundamentals while solving STEM based projects and tapping into their creative minds.</p>
  </div>
  <div class="abs brand">bytesprout</div>

  <div class="abs classes">
    <h2>BEGINNER BLOKIT</h2>
    <ul>
      <li>For kids new to coding. Learn to program using Blokit, a fun and easy to use language. Make games, interactive stories, animations, and more, all while learning the fundamentals of computer programming.</li>
      <li>For students with little or no experience.</li>
    </ul>
    <h2>INTERMEDIATE<br>BLOKIT</h2>
    <ul>
      <li>Kids learn more advanced programming concepts in Blokit and create larger and more complex programs. They plan, design, and create their own coding projects, from start to finish.</li>
      <li>For students who have completed Beginner Blokit 1 &amp; 2 or have prior coding experience.</li>
    </ul>
    <h2>BUILDER BENCH<br>WORKSHOP</h2>
    <ul>
      <li>Continue to learn and explore coding in a collaborative, fun space. Each lesson kids complete a new, STEM based coding project. Projects cover Physics, Math, Story Telling, Game Design, Brick Robotics, and more.</li>
      <li>Recommended for intermediate students.</li>
    </ul>
    <h2>PYLON</h2>
    <ul>
      <li>Learn to code in one of the most popular text based languages. Pylon 101 teaches kids the basics of Pylon coding with an emphasis on Mathematics and computer science fundamentals.</li>
      <li>For students aged 12-17 with little or no experience.</li>
    </ul>
  </div>
</section>

</body>
</html>
```